Kelvo Marine business card

We sell live saltwater fish and live corals
Kelvo Marine
7 Harlow Ct
Ardenvale, PA. 17342
(555) 555-0147
Contact Information for Business Card
Kelvo Marine
7 Harlow Ct
Ardenvale, PA. 17342
(555) 555-0147
Colors
Designer to choose colors to be used in the design.

```html
<!DOCTYPE html>
<html lang="en">
<head>
<meta charset="utf-8">
<title>Kelvo Marine business card</title>
<link rel="stylesheet" href="https://fonts.googleapis.com/css2?family=Crimson+Text:ital,wght@0,400;0,600;1,600;1,700&display=swap">
<style>
  :root {
    --page: #fefefe;
    --navy: #1b4d91;
    --navy-deep: #154a8c;
    --navy-light: #22529d;
    --sky: #0285cb;
    --sky-bright: #1aa3e8;
    --panel: #fdfdfd;
    --brand: #36469b;
    --ink-light: #ffffff;
  }
  * { margin: 0; padding: 0; box-sizing: border-box; }
  html, body { width: 1200px; height: 1200px; overflow: hidden; background: var(--page); }
  .canvas { position: relative; width: 1200px; height: 1200px; }
  .card {
    position: absolute; left: 158px; top: 348px; width: 884px; height: 504px;
    overflow: hidden;
    background: linear-gradient(100deg, var(--navy-light) 0%, var(--navy-deep) 40%, var(--navy) 70%, var(--navy-light) 100%);
    font-family: "Crimson Text", serif;
  }
  .card-shapes { position: absolute; inset: 0; }
  .tagline {
    position: absolute; left: 0; top: 242px; width: 342px; height: 62px;
    color: var(--ink-light); text-align: center; font-style: italic; font-weight: 600;
    font-size: 15px; line-height: 21px; padding-top: 9px;
  }
  .tagline-lead { display: flex; align-items: center; justify-content: center; gap: 6px; }
  .tagline-lead::before, .tagline-lead::after {
    content: ""; width: 76px; height: 1px; background: var(--sky-bright);
  }
  .brand {
    position: absolute; left: 580px; top: 62px; width: 202px; text-align: center;
    color: var(--brand);
  }
  .brand-dot {
    width: 104px; height: 104px; border-radius: 50%; margin: 0 auto 14px;
    background: linear-gradient(180deg, #a8dcf5 0%, #cfeefb 55%, #3aa6de 100%);
  }
  .brand-name { font-weight: 600; font-size: 44px; line-height: 42px; }
  .contact {
    position: absolute; left: 48px; color: var(--ink-light);
    font-size: 22px; line-height: 31px; display: flex; gap: 12px;
  }
  .contact svg { flex: none; margin-top: 6px; }
  .contact-address { top: 336px; }
  .contact-phone { top: 411px; }
</style>
</head>
<body>
<div class="canvas">
  <div class="card">
    <svg class="card-shapes" width="884" height="504" viewBox="0 0 884 504">
      <defs>
        <linearGradient id="meshTop" x1="0" y1="0" x2="0" y2="1">
          <stop offset="0" stop-color="#1f6fb8" stop-opacity="0.35"/>
          <stop offset="1" stop-color="#1f6fb8" stop-opacity="0"/>
        </linearGradient>
        <linearGradient id="meshBottom" x1="0" y1="1" x2="0" y2="0">
          <stop offset="0" stop-color="#1f6fb8" stop-opacity="0.35"/>
          <stop offset="1" stop-color="#1f6fb8" stop-opacity="0"/>
        </linearGradient>
      </defs>
      <rect class="mesh-area" role="img" aria-label="Low-poly line mesh texture" x="0" y="0" width="400" height="200" fill="url(#meshTop)"/>
      <rect class="mesh-area" role="img" aria-label="Low-poly line mesh texture" x="280" y="320" width="604" height="184" fill="url(#meshBottom)"/>
      <polygon class="accent-band" points="397,0 579,427 884,278 884,252 610,396 410,0" fill="var(--sky)"/>
      <polygon class="logo-panel" points="410,0 884,0 884,252 610,396" fill="var(--panel)"/>
      <polygon class="tagline-ribbon" points="0,242 315,242 347,304 0,304" fill="var(--sky)"/>
    </svg>

    <div class="tagline">
      <div class="tagline-lead">We Sell</div>
      <div>Live Saltwater Fish and Live Corals</div>
    </div>

    <div class="brand">
      <div class="brand-dot"></div>
      <div class="brand-name">Kelvo<br>Marine</div>
    </div>

    <div class="contact contact-address">
      <svg width="14" height="18" viewBox="0 0 14 18" aria-hidden="true">
        <path d="M7 0C3.1 0 0 3 0 6.8 0 11.5 7 18 7 18s7-6.5 7-11.2C14 3 10.9 0 7 0z" fill="var(--sky-bright)"/>
        <circle cx="7" cy="6.6" r="2.2" fill="var(--navy)"/>
      </svg>
      <div>Kelvo Marine 7 Harlow<br>Ct Ardenvale, PA</div>
    </div>

    <div class="contact contact-phone">
      <svg width="14" height="18" viewBox="0 0 14 18" aria-hidden="true">
        <path d="M3 1.5l2.6 3.4-1.7 1.6c.6 2.6 2 4.9 4.1 6.6l1.8-1.3 3 3-1.8 1.9C6 15.9 1.6 10 1.1 3.2z" fill="none" stroke="var(--sky-bright)" stroke-width="1.4" stroke-linejoin="round"/>
      </svg>
      <div>17342 (555) 555-0147</div>
    </div>
  </div>
</div>
</body>
</html>
```